Gardowell - Direct Mail DL flyer design

Create a direct market flyer (d/l size) to compel people to act and visit our website to buy life insurance.

Copy, example images and notes are provided

Target Market(s)

Families with debt who need life insurance

Industry/Entity Type

Insurance

Requirements
Must have
• Our logo
• Colours are Blue C99, M79, Y0, K0 Green C40, M0, Y100, K0
• Copy side 1 is "For the price of a coffee you can ensure you and your family get the right start."
• Copy side 2 is "It doesn't sound like much, but when it comes to life insurance, $1 a day* can make a huge difference if you were to die.
• For the cost of a cup of coffee a day, you can ensure your family will be left with enough to protect the home, pay for ongoing living expenses and fund your children's continued education.
• Your life is important
• Apply today and get 1 month free cover
• Build your tomorrow
• company logo gardowell.com.au make prominant
• *For a monthly premium of $25.33, a 35 year old non-smoking male can obtain $300,000 of term life cover.
• Example for illistration purpose only. The premium cited is current as at February 2016, is based on the factors referred to in the example and subject to underwriting. You should consider whether this product is appropriate for you. Refer to the Product Disclosure Statement, available from gardowell before deciding whether to acquire the product."
• Footer
• Gardowell Pty Ltd
• ABN 47 253 918 604 AFS Licence 729140
Nice to have
• Coffee cup with pods/capsuals around it white background side 1 and coffee ring stain on reverse as watermark
• Trusafe has been awarded - Merrow Ratings - 2014 Kestrel Protection Honours for Term Cover
• Trusafe has been awarded - Merrow Ratings - 2015 Kestrel Protection Honours for Term Cover

```html
<!DOCTYPE html>
<html lang="en">
<head>
<meta charset="utf-8">
<title>Gardowell – DL Flyer</title>
<link href="https://fonts.googleapis.com/css2?family=Didact+Gothic&family=Mulish:wght@600;700&display=swap" rel="stylesheet">
<style>
  :root {
    --stage: #2e2e2e;
    --green: #5fc61c;
    --green-light: #8ee04a;
    --green-deep: #4fb814;
    --blue: #1f7fd0;
    --blue-light: #3fa0e6;
    --navy: #1d3f8f;
    --white: #ffffff;
    --ink: #2a2a2a;
    --fine-ink: #2f4a1a;
    --paper: #e9eaea;
  }
  * { box-sizing: border-box; margin: 0; padding: 0; }
  html, body { width: 1200px; height: 900px; overflow: hidden; }
  body {
    background: var(--stage);
    position: relative;
    font-family: "Didact Gothic", "Century Gothic", sans-serif;
    color: var(--white);
  }
  .flyer {
    position: absolute;
    top: 60px;
    width: 390px;
    height: 780px;
    background: radial-gradient(ellipse at 50% 45%, var(--green-light) 0%, var(--green) 45%, var(--green-deep) 100%);
    overflow: hidden;
    text-align: center;
  }
  .flyer--front { left: 143px; }
  .flyer--back { left: 640px; }

  .quote-mark {
    position: absolute;
    left: 0; right: 0;
    display: flex;
    align-items: center;
    justify-content: center;
    gap: 18px;
    font-family: "Mulish", sans-serif;
    font-weight: 700;
    font-size: 46px;
    line-height: 1;
    height: 30px;
  }
  .quote-mark::before, .quote-mark::after {
    content: "";
    width: 80px;
    height: 1px;
    background: rgba(255,255,255,0.8);
  }
  .quote-mark span { display: block; height: 30px; padding-top: 2px; }
  .quote-mark--open-front { top: 42px; }
  .quote-mark--close-front { top: 262px; }
  .quote-mark--open-back { top: 26px; }

  .front-headline {
    position: absolute;
    top: 86px; left: 0; right: 0;
    font-weight: 400;
    font-size: 31px;
    line-height: 37.5px;
    white-space: nowrap;
  }
  .cup-photo {
    position: absolute;
    top: 318px; left: 108px;
    width: 174px; height: 316px;
    border-radius: 10px;
    background: linear-gradient(180deg, #f4f4f2 0%, #d9cbb5 55%, #eeeeec 100%);
  }
  .brand-band {
    position: absolute;
    left: 0; right: 0;
    background: var(--white);
    display: flex;
    align-items: center;
  }
  .flyer--front .brand-band { top: 688px; height: 68px; justify-content: center; }
  .brand {
    display: flex;
    align-items: center;
    gap: 8px;
  }
  .brand-mark {
    width: 30px; height: 30px;
    background: var(--navy);
    border-radius: 4px;
  }
  .brand-text { text-align: left; }
  .brand-name {
    font-size: 27px;
    color: var(--navy);
    line-height: 1;
  }
  .brand-tag {
    font-size: 11px;
    letter-spacing: 1.5px;
    color: var(--navy);
    margin-top: 2px;
  }

  .back-lead {
    position: absolute;
    top: 61px; left: 0; right: 0;
    font-size: 19px;
    line-height: 24.3px;
    white-space: nowrap;
  }
  .back-lead p + p { margin-top: 12px; }
  .life-banner {
    position: absolute;
    top: 330px; left: 16px;
    width: 358px; height: 35px;
    background: linear-gradient(180deg, var(--blue-light), var(--blue));
    font-family: "Mulish", sans-serif;
    font-weight: 700;
    font-size: 23px;
    line-height: 35px;
    box-shadow: 0 2px 4px rgba(0,0,0,0.25);
  }
  .offer {
    position: absolute;
    top: 376px; left: 0; right: 0;
    font-size: 17px;
  }
  .slogan {
    position: absolute;
    top: 396px; left: 0; right: 0;
    font-family: "Mulish", sans-serif;
    font-weight: 700;
    font-size: 31px;
  }
  .stain-photo {
    position: absolute;
    top: 442px; left: 0; right: 0;
    height: 166px;
    background: linear-gradient(180deg, #f1f1f1, var(--paper));
  }
  .fine-print {
    position: absolute;
    top: 619px; left: 18px; right: 18px;
    color: var(--fine-ink);
    font-size: 8.4px;
    line-height: 10.4px;
  }
  .fine-print .premium { font-size: 9.2px; padding: 0 40px; margin-bottom: 3px; }
  .flyer--back .brand-band { top: 692px; height: 78px; justify-content: space-between; padding: 0 16px 0 26px; }
  .company {
    text-align: left;
    color: var(--ink);
    font-size: 12.5px;
    line-height: 16px;
  }
  .flyer--back .brand-name { font-size: 22px; }
  .flyer--back .brand-mark { width: 26px; height: 26px; }
  .flyer--back .brand-tag { font-size: 9px; }
</style>
</head>
<body>
  <section class="flyer flyer--front">
    <div class="quote-mark quote-mark--open-front"><span>“</span></div>
    <h1 class="front-headline">For the price of a<br>Coffee you can Ensure<br>you and your family<br>get the right start</h1>
    <div class="quote-mark quote-mark--close-front"><span>”</span></div>
    <div class="cup-photo" role="img" aria-label="Photo of a takeaway coffee cup with a black lid and a cardboard sleeve"></div>
    <div class="brand-band">
      <div class="brand">
        <div class="brand-mark"></div>
        <div class="brand-text">
          <div class="brand-name">gardowell.com.au</div>
          <div class="brand-tag">build your tomorrow</div>
        </div>
      </div>
    </div>
  </section>

  <section class="flyer flyer--back">
    <div class="quote-mark quote-mark--open-back"><span>“</span></div>
    <div class="back-lead">
      <p>It doesn't sound like much, but<br>when it comes to life insurance,<br>$1 a day* can make a<br>huge difference if you were to die.</p>
      <p>For the cost of a cup of coffee a day,<br>you can ensure your family will be<br>left with enough to protect the<br>home, pay for ongoing living<br>expenses and fund your children's<br>continued education.</p>
    </div>
    <div class="life-banner">YOUR LIFE IS IMPORTANT</div>
    <p class="offer">Apply today and get 1 month free cover</p>
    <p class="slogan">Build your tomorrow</p>
    <div class="stain-photo" role="img" aria-label="Coffee ring stain on white paper"></div>
    <div class="fine-print">
      <p class="premium">*For a monthly premium of $25.33, a 35 year old non-smoking male can obtain $300,000 of term life cover.</p>
      <p>Example for illustration purpose only. The premium cited is current as at February 2016, is based on the factors referred to in the example and subject to underwriting. You should consider whether this product is appropriate for you. Refer to the Product Disclosure Statement, available from gardowell before deciding whether to acquire the product.*</p>
    </div>
    <div class="brand-band">
      <div class="company">
        <p>Gardowell Pty Ltd</p>
        <p>ABN 47 253 918 604</p>
        <p>AFS Licence 729140</p>
      </div>
      <div class="brand">
        <div class="brand-mark"></div>
        <div class="brand-text">
          <div class="brand-name">gardowell.com.au</div>
          <div class="brand-tag">build your tomorrow</div>
        </div>
      </div>
    </div>
  </section>
</body>
</html>
```